Business Card Design Project

Hi,

We are a new modern sheet metal business and I require a business card for our sales reps.

The card should be double sided and standout in a crowd.

I have attached our logo and our website is www.folvik.com.au.

Please ask if you have any further questions
Updates

hi everyone, 

I'm wondering if we can try to lighten the cards mood.  Everyone is using black and I'm not sure how that would be accepted in real life.

Gregory

Reason: Still No receiving what I was hoping for.

Industry/Entity Type

Business

Requirements
Must have
• double sided

```html
<!DOCTYPE html>
<html lang="en">
<head>
<meta charset="utf-8">
<title>Folvik Sheetmetal – Business Card</title>
<link rel="stylesheet" href="https://fonts.googleapis.com/css2?family=Arimo:wght@400;700&display=swap">
<style>
  :root {
    --page: #d9d9d9;
    --card-dark: #333233;
    --card-blue: #15337a;
    --back-light: #ffffff;
    --back-edge: #5a5a5a;
    --mark-faint: rgba(200, 205, 220, 0.55);
    --text-light: #ffffff;
    --tagline: #9a9a9a;
  }
  * { margin: 0; padding: 0; box-sizing: border-box; }
  html, body {
    width: 1200px; height: 901px; overflow: hidden;
    background: var(--page);
    font-family: "Arimo", Arial, sans-serif;
  }
  .canvas {
    position: relative; width: 1200px; height: 901px;
  }
  .card {
    position: absolute; top: 296px;
    width: 540px; height: 309px;
    overflow: hidden;
    box-shadow: 0 4px 12px rgba(0,0,0,0.25);
  }
  /* Back side */
  .card-back {
    left: 45px;
    background: radial-gradient(ellipse at 50% 45%, var(--back-light) 0%, #bdbdbd 45%, var(--back-edge) 100%);
    border: 2px solid #fff;
  }
  .back-heading {
    position: absolute; top: 30px; left: 0; width: 100%;
    text-align: center;
    color: var(--text-light); font-size: 22px; letter-spacing: 0.5px;
  }
  .back-mark {
    position: absolute; top: 105px; left: 0; width: 100%;
    text-align: center;
    color: var(--mark-faint); font-weight: 700; font-size: 96px; letter-spacing: 2px;
  }
  .back-tagline {
    position: absolute; top: 220px; left: 0; width: 100%;
    text-align: center;
    color: var(--mark-faint); font-size: 14px; letter-spacing: 1px;
  }
  /* Front side */
  .card-front { left: 615px; background: var(--card-dark); }
  .front-wave { position: absolute; inset: 0; }
  .front-wave path { fill: var(--card-blue); }
  .brand {
    position: absolute; top: 38px; left: 58px;
    display: flex; align-items: center; gap: 10px;
  }
  .brand-square { width: 22px; height: 22px; background: var(--card-blue); }
  .brand-name {
    color: var(--text-light); font-weight: 700; font-size: 30px; letter-spacing: 1px;
  }
  .brand-tagline {
    position: absolute; top: 82px; left: 58px;
    color: var(--tagline); font-size: 8px; letter-spacing: 0.5px;
  }
  .rep-name {
    position: absolute; top: 140px; left: 345px;
    color: var(--text-light); font-size: 19px;
  }
  .contact-list {
    position: absolute; top: 200px; left: 35px;
    list-style: none; color: var(--text-light); font-size: 19px; line-height: 23px;
  }
</style>
</head>
<body>
<main class="canvas">
  <section class="card card-back" aria-label="Card back">
    <p class="back-heading">OTHER DETAILS</p>
    <p class="back-mark">FOLVIK</p>
    <p class="back-tagline">Flashings | Gutter | Rainwater Goods</p>
  </section>

  <section class="card card-front" aria-label="Card front">
    <svg class="front-wave" viewBox="0 0 540 309" preserveAspectRatio="none" aria-hidden="true">
      <path d="M0,170 C40,150 80,132 150,135 C260,140 330,268 455,268 C500,268 525,255 540,245 L540,309 L0,309 Z"/>
    </svg>
    <div class="brand">
      <span class="brand-square"></span>
      <span class="brand-name">FOLVIK</span>
    </div>
    <p class="brand-tagline">Flashings · Gutter · Rainwater Goods</p>
    <p class="rep-name">NAME</p>
    <ul class="contact-list">
      <li>ADD.</li>
      <li>MO.</li>
      <li>WEBSITE</li>
      <li>E-mail</li>
    </ul>
  </section>
</main>
</body>
</html>
```